Awesome photographers card for an awesome new business

Double sided business card Black background and silver logo in middle on one side. Details on otherside. please keep it simple

Industry/Entity Type

Photographer

Contact Information for Business Card

Colin Fairweather
0452816307
ColinFairweatherPhotography57@mailvane.com
www.ColinFairweatherPhotography.com.au
Instagram _Colin_fairweather

Requirements
Must have
• My logo in Silver
• please use instagram logo instead of "Instagram"

```html
<!DOCTYPE html>
<html lang="en">
<head>
<meta charset="utf-8">
<title>Colin Fairweather Photography – Business Card</title>
<link rel="stylesheet" href="https://fonts.googleapis.com/css2?family=Great+Vibes&family=Open+Sans:wght@400;600&display=swap">
<style>
  :root {
    --canvas-bg: #c9c9c9;
    --card-black: #1c1c1c;
    --silver: #a9a9a9;
    --ghost-mark: #0c0c0c;
    --contact-grey: #6d6d6d;
    --icon-box: #3a3a3a;
    --icon-glyph: #1c1c1c;
    --signature: #e6e6e6;
    --rule: #3c3c3c;
  }
  * { margin: 0; padding: 0; box-sizing: border-box; }
  html, body {
    width: 1200px; height: 1014px; overflow: hidden;
    background: var(--canvas-bg);
    font-family: "Open Sans", Arial, sans-serif;
  }
  .canvas { position: relative; width: 1200px; height: 1014px; }

  .card {
    position: absolute;
    width: 630px; height: 360px;
    background: var(--card-black);
    box-shadow: 0 10px 24px rgba(0,0,0,.28);
  }
  .card--front { left: 60px; top: 70px; }
  .card--back  { left: 510px; top: 584px; }

  /* Front: brand name in silver, centred */
  .brand {
    position: absolute; inset: 0;
    display: flex; align-items: center; justify-content: center; gap: 18px;
  }
  .brand__dot {
    width: 16px; height: 16px; border-radius: 50%;
    background: var(--silver);
  }
  .brand__name {
    font-weight: 600; font-size: 30px; letter-spacing: 6px;
    text-transform: uppercase; color: var(--silver);
  }

  /* Back: faint brand mark top right */
  .brand--ghost {
    inset: auto; right: 40px; top: 60px; gap: 10px;
  }
  .brand--ghost .brand__dot { width: 10px; height: 10px; background: var(--ghost-mark); }
  .brand--ghost .brand__name { font-size: 17px; letter-spacing: 3px; color: var(--ghost-mark); }

  .details {
    position: absolute; left: 48px; top: 150px; bottom: 22px;
    border-left: 1px solid var(--rule);
    padding-left: 24px;
  }
  .details__name {
    font-family: "Great Vibes", cursive;
    font-size: 44px; color: var(--signature);
    line-height: 1; margin-bottom: 22px; margin-left: 4px;
  }
  .contact-list { list-style: none; }
  .contact-list li {
    display: flex; align-items: center; gap: 14px;
    height: 30px; font-size: 15px; color: var(--contact-grey);
  }
  .contact-icon {
    width: 22px; height: 22px; border-radius: 3px;
    background: var(--icon-box);
    display: flex; align-items: center; justify-content: center;
    flex: none;
  }
  .contact-icon svg { width: 14px; height: 14px; }
</style>
</head>
<body>
<main class="canvas">

  <section class="card card--front" aria-label="Card front">
    <div class="brand">
      <span class="brand__dot"></span>
      <span class="brand__name">Colin Fairweather</span>
    </div>
  </section>

  <section class="card card--back" aria-label="Card back">
    <div class="brand brand--ghost">
      <span class="brand__dot"></span>
      <span class="brand__name">Colin Fairweather</span>
    </div>

    <div class="details">
      <p class="details__name">Colin Fairweather</p>
      <ul class="contact-list">
        <li>
          <span class="contact-icon">
            <svg viewBox="0 0 24 24"><path fill="var(--icon-glyph)" d="M6.6 10.8a15.1 15.1 0 0 0 6.6 6.6l2.2-2.2a1 1 0 0 1 1-.25 11.4 11.4 0 0 0 3.6.57 1 1 0 0 1 1 1V20a1 1 0 0 1-1 1A17 17 0 0 1 3 4a1 1 0 0 1 1-1h3.5a1 1 0 0 1 1 1c0 1.25.2 2.45.57 3.57a1 1 0 0 1-.25 1z"/></svg>
          </span>
          0452816307
        </li>
        <li>
          <span class="contact-icon" aria-label="Instagram">
            <svg viewBox="0 0 24 24"><rect x="3" y="3" width="18" height="18" rx="5" fill="none" stroke="var(--icon-glyph)" stroke-width="2.5"/></svg>
          </span>
          Colin_fairweather
        </li>
        <li>
          <span class="contact-icon">
            <svg viewBox="0 0 24 24"><rect x="2" y="5" width="20" height="14" fill="none" stroke="var(--icon-glyph)" stroke-width="2"/><path d="M2 5l10 8 10-8" fill="none" stroke="var(--icon-glyph)" stroke-width="2"/></svg>
          </span>
          ColinFairweatherPhotography57@mailvane.com
        </li>
        <li>
          <span class="contact-icon">
            <svg viewBox="0 0 24 24"><circle cx="12" cy="12" r="9" fill="none" stroke="var(--icon-glyph)" stroke-width="2"/><ellipse cx="12" cy="12" rx="4" ry="9" fill="none" stroke="var(--icon-glyph)" stroke-width="1.6"/><path d="M3 12h18M5 7h14M5 17h14" stroke="var(--icon-glyph)" stroke-width="1.4"/></svg>
          </span>
          www.ColinFairweatherPhotography.com.au
        </li>
      </ul>
    </div>
  </section>

</main>
</body>
</html>
```